Lantern Hill Publicity is a new boutique Press Office with a small roster of well-chosen clients across an array of disciplines; from Art and Technology to Restaurants and Fashion. Based in Greenpoint Brooklyn, Lantern Hill Publicity achieves outstanding results through hard work, tenacity, efficiency and a sense of humor. We need a simple, versatile and classic design. We would like each side of the card to be white text on a black background.

Boutique

```html
<!DOCTYPE html>
<html lang="en">
<head>
<meta charset="utf-8">
<title>Lantern Hill Publicity — Business Card</title>
<link href="https://fonts.googleapis.com/css2?family=Cinzel:wght@400;600&family=Montserrat:wght@400;500&display=swap" rel="stylesheet">
<style>
  :root {
    --page: #e9e6e2;
    --card: #0b0b0b;
    --card-edge: #1c1c1c;
    --ink: #ffffff;
    --ink-soft: #d9d9d9;
    --rule: #8a8a8a;
  }
  * { box-sizing: border-box; margin: 0; padding: 0; }
  html, body { width: 1200px; height: 913px; overflow: hidden; }
  body {
    background: var(--page);
    position: relative;
    font-family: "Montserrat", Arial, sans-serif;
    color: var(--ink);
  }
  .card {
    position: absolute;
    left: 340px;
    width: 520px;
    height: 297px;
    background: linear-gradient(135deg, #161616 0%, var(--card) 55%, #050505 100%);
    border-radius: 14px;
    border: 1px solid var(--card-edge);
    overflow: hidden;
  }
  .card--front { top: 120px; }
  .card--back { top: 496px; }

  /* front */
  .front__tab {
    position: absolute;
    top: -10px;
    right: 24px;
    width: 30px;
    height: 96px;
    background: var(--ink);
    border-radius: 0 0 14px 14px;
  }
  .front__brand {
    position: absolute;
    left: 34px;
    top: 108px;
    width: 200px;
    font-family: "Cinzel", Georgia, serif;
    font-weight: 600;
    font-size: 30px;
    line-height: 1.15;
    letter-spacing: 1px;
  }
  .front__divider {
    position: absolute;
    left: 258px;
    top: 60px;
    width: 1px;
    height: 170px;
    background: linear-gradient(180deg, transparent, var(--rule) 20%, var(--rule) 80%, transparent);
  }
  .front__details {
    position: absolute;
    left: 282px;
    top: 44px;
  }
  .details__name {
    font-family: "Cinzel", Georgia, serif;
    font-weight: 600;
    font-size: 19px;
    letter-spacing: 0.5px;
    margin-bottom: 4px;
  }
  .details__line {
    font-size: 12.5px;
    line-height: 20px;
    color: var(--ink-soft);
  }
  .contact-list { list-style: none; margin-top: 6px; }
  .contact-list li {
    display: flex;
    align-items: center;
    gap: 9px;
    font-size: 12.5px;
    line-height: 21px;
    color: var(--ink-soft);
  }
  .contact-list svg { width: 11px; height: 11px; flex: none; }

  /* back */
  .back__brand {
    position: absolute;
    left: 0;
    right: 0;
    top: 92px;
    text-align: center;
  }
  .back__name {
    font-family: "Cinzel", Georgia, serif;
    font-weight: 600;
    font-size: 34px;
    letter-spacing: 4px;
    line-height: 1;
  }
  .back__sub {
    font-family: "Cinzel", Georgia, serif;
    font-weight: 400;
    font-size: 12px;
    letter-spacing: 9px;
    margin-top: 8px;
    color: var(--ink-soft);
  }
  .back__web {
    position: absolute;
    left: 0;
    right: 0;
    top: 218px;
    text-align: center;
    font-weight: 500;
    font-size: 15px;
    letter-spacing: 0.5px;
  }
</style>
</head>
<body>

<section class="card card--front" aria-label="Card front">
  <div class="front__tab"></div>
  <div class="front__brand">Lantern Hill Publicity</div>
  <div class="front__divider"></div>
  <div class="front__details">
    <p class="details__name">MARCUS ELLERY</p>
    <p class="details__line">Director</p>
    <p class="details__line">1420 Harbor View Rd #112</p>
    <p class="details__line">Tampa, FL 33602</p>
    <ul class="contact-list">
      <li>
        <svg viewBox="0 0 12 12" fill="none" stroke="currentColor" stroke-width="1.2"><rect x="3" y="0.8" width="6" height="10.4" rx="1"/><line x1="5" y1="9.4" x2="7" y2="9.4"/></svg>
        +330 5812-4093
      </li>
      <li>
        <svg viewBox="0 0 12 12" fill="currentColor"><path d="M1 4.5C1 2.5 3 2 6 2s5 .5 5 2.5L9 5.2 8.2 3.8H3.8L3 5.2Z"/><rect x="2.5" y="6" width="7" height="4.5" rx="1"/></svg>
        +330 5812-4170
      </li>
      <li>
        <svg viewBox="0 0 12 12" fill="none" stroke="currentColor" stroke-width="1.2"><rect x="1" y="2.5" width="10" height="7" rx="0.8"/><polyline points="1.3,3 6,6.5 10.7,3"/></svg>
        hello@lanternhill.com
      </li>
      <li>
        <svg viewBox="0 0 12 12" fill="none" stroke="currentColor" stroke-width="1.1"><circle cx="6" cy="6" r="5"/><ellipse cx="6" cy="6" rx="2.2" ry="5"/><line x1="1" y1="6" x2="11" y2="6"/></svg>
        www.lanternhill.com
      </li>
    </ul>
  </div>
</section>

<section class="card card--back" aria-label="Card back">
  <div class="back__brand">
    <p class="back__name">LANTERN HILL</p>
    <p class="back__sub">PUBLICITY</p>
  </div>
  <p class="back__web">www.lanternhill.com</p>
</section>

</body>
</html>
```